qm - website template
website of specialist in neurosurgery, and teacher at the University in Milan
qm - website template - Education
Creative Brief
Education
Benedetto L. Caramuzza, MD (specialist in neurosurgery and in the history of medicine), historian and anthropologist, teaches history of medicine and health in the Faculty of Medicine, University of Velmora Castrene, where he directs the Institute for anatomical inquiry into past doctrines "(www.dulrota.it).
He's the author of over 250 papers in national and international partner to the history of medical and health disciplines and pharmacological institute of the Italian Ombrilla.
Traditional
blu (see attached logo file)
red (see attached logo file)
We need the graphic template of: • Homepage • Generic content page (text+image+ eventual document to download) • listing page of books + page with information about the selected book • listing page of conference + page with information about the selected conference • Contact The site must be optimized for 1024X768. For the main menu, it's possibile to use not system font. File must be preferably png (adobe fireworks), otherwise ai (adobe illustrator) or psd (adobe photoshop).

```html
<!DOCTYPE html>
<html lang="it">
<head>
<meta charset="utf-8">
<title>Benedetto L. Caramuzza – Book Listing</title>
<link rel="stylesheet" href="https://fonts.googleapis.com/css2?family=Ubuntu:wght@400;500;700&family=Arimo:wght@400;700&display=swap">
<style>
:root{
  --page-bg:#e9e9e9;
  --panel:#ffffff;
  --nav-top:#2b5f93;
  --nav-bottom:#183f69;
  --accent-red:#c4222b;
  --accent-red-dark:#9d1820;
  --heading:#1b1b1b;
  --text:#6a6a6a;
  --muted:#8c8c8c;
  --link-blue:#2a5d8f;
  --rule:#e3e3e3;
  --cover-dark:#141414;
  --cover-red:#8e1a12;
}
*{box-sizing:border-box;margin:0;padding:0}
html,body{width:1200px;height:932px;overflow:hidden}
body{
  position:relative;
  background:linear-gradient(180deg,#f3f3f3 0%,var(--page-bg) 60%,#e2e2e2 100%);
  font-family:"Arimo",Arial,sans-serif;color:var(--text);
}
.language{position:absolute;top:33px;left:986px;display:flex;align-items:center;gap:6px;font-size:12px;color:#444}
.language svg{display:block}
.main-nav{
  position:absolute;left:98px;top:68px;width:998px;height:51px;
  background:linear-gradient(180deg,var(--nav-top),var(--nav-bottom));
  border-radius:3px;box-shadow:0 2px 4px rgba(0,0,0,.2);
  font-family:"Ubuntu",sans-serif;font-weight:500;font-size:14.5px;color:#fff;
}
.main-nav a{color:#fff;text-decoration:none;position:absolute;top:0;height:51px;line-height:51px;white-space:nowrap}
.main-nav .active{
  left:0;width:104px;text-align:center;
  background:linear-gradient(180deg,var(--accent-red),var(--accent-red-dark));
  border-radius:3px 0 0 3px;
}
.content-panel{
  position:absolute;left:98px;top:131px;width:998px;height:657px;
  background:var(--panel);border-radius:3px;
  box-shadow:0 1px 5px rgba(0,0,0,.12);
}
.breadcrumb{position:absolute;left:31px;top:22px;font-size:12.5px;color:var(--muted)}
.breadcrumb span{color:var(--accent-red);margin:0 6px}
.breadcrumb a{color:var(--accent-red);text-decoration:none}
.book-cover{
  position:absolute;left:31px;top:66px;width:240px;height:254px;
  background:linear-gradient(180deg,var(--cover-dark) 0%,#1e1515 40%,var(--cover-red) 62%,#2a0c08 80%,var(--cover-dark) 100%);
}
.book-title{
  position:absolute;left:296px;top:58px;width:440px;
  font-family:"Ubuntu",sans-serif;font-weight:700;font-size:27px;line-height:30px;color:var(--heading);
}
.book-text{position:absolute;left:296px;width:384px;font-size:12.3px;line-height:14.6px}
.book-text.first{top:133px}
.book-text.second{top:251px}
.book-text em{color:var(--accent-red)}
.full-text{position:absolute;left:31px;top:344px;width:675px;font-size:12.3px;line-height:14.6px}
.heading-sample{position:absolute;left:31px;font-family:"Ubuntu",sans-serif;font-weight:700;color:var(--heading);line-height:1}
.h1s{top:452px;font-size:29px}
.h2s{top:484px;font-size:24px}
.h3s{top:522px;font-size:17px}
.h4s{top:552px;font-size:13px}
.h5s{top:583px;font-size:11px}
.h6s{top:614px;font-size:10px}
.sidebar-box{position:absolute;left:768px;width:220px;padding-bottom:16px;border-bottom:1px solid var(--rule);box-shadow:0 6px 6px -6px rgba(0,0,0,.18)}
.sidebar-box h3{font-family:"Ubuntu",sans-serif;font-weight:500;font-size:17px;color:var(--heading);margin-bottom:10px}
.sidebar-box ul{list-style:none}
.sidebar-box li{font-size:11.5px;line-height:15px;color:var(--text);padding-left:13px;position:relative}
.sidebar-box li::before{content:"";position:absolute;left:2px;top:4px;border-left:6px solid var(--link-blue);border-top:3.5px solid transparent;border-bottom:3.5px solid transparent}
.box-books{top:30px}
.box-papers{top:154px}
.box-talks{top:290px;border-bottom:none;box-shadow:none}
.footer-note{position:absolute;left:98px;top:824px;font-size:12px;color:#777}
.social-links{position:absolute;left:948px;top:822px;display:flex;gap:9px;font-size:11px;color:var(--link-blue)}
.social-links a{display:flex;align-items:center;gap:3px;color:var(--link-blue);text-decoration:none}
.social-links i{display:block;width:12px;height:12px;background:var(--link-blue)}
</style>
</head>
<body>
<div class="language">Language
  <svg width="28" height="11" viewBox="0 0 28 11" aria-hidden="true">
    <rect x="0" y="0" width="4" height="11" fill="#1d8a3e"/><rect x="4" y="0" width="4" height="11" fill="#fff"/><rect x="8" y="0" width="4" height="11" fill="#d52b2b"/>
    <rect x="15" y="0" width="13" height="11" fill="#fff" stroke="#ddd" stroke-width=".5"/><rect x="20" y="0" width="3" height="11" fill="#d52b2b"/><rect x="15" y="4" width="13" height="3" fill="#d52b2b"/>
  </svg>
</div>

<nav class="main-nav">
  <a class="active" href="#">Biografia</a>
  <a href="#" style="left:130px">Libri</a>
  <a href="#" style="left:187px">Pubblicazioni scientifiche</a>
  <a href="#" style="left:387px">Conferenze</a>
  <a href="#" style="left:492px">Attivita didattica</a>
  <a href="#" style="left:645px">Attivita medica</a>
  <a href="#" style="left:781px">News</a>
  <a href="#" style="left:854px">Link</a>
  <a href="#" style="left:917px">Contatti</a>
</nav>

<main class="content-panel">
  <div class="breadcrumb">Biografia<span>»</span><a href="#">Book Listing</a></div>
  <div class="book-cover" role="img" aria-label="Book cover of The Cortical Architecture of Memory by Edwin R. Haldane"></div>
  <h1 class="book-title">The Cortical Architecture<br>of Memory</h1>
  <p class="book-text first">Lorem ipsum dolor sit amet, consectetuer adipiscing elit, sed diam nonummy nibh euismod tincidunt ut laoreet dolore magna aliquam erat volutpat. <em>Ut wisi enim ad minim veniam</em> , quis nostrud exerci tation ullamcorper suscipit lobortis nisl ut aliquip ex ea commodo consequat.</p>
  <p class="book-text second">Duis autem vel eum iriure dolor in hendrerit in vulputate velit esse molestie consequat, vel illum dolore eu feugiat nulla facilisis at vero eros et accumsan et iusto odio dignissim qui blandit praesent luptatum zzril delenit augue duis dolore te feugait nulla facilisi.</p>
  <p class="full-text">Nam liber tempor cum soluta nobis eleifend option congue nihil imperdiet doming id quod mazim placerat facer possim assum. Typi non habent claritatem insitam; est usus legentis in iis qui facit eorum claritatem. Investigationes demonstraverunt lectores legere me lius quod ii legunt saepius. Claritas est etiam processus dynamicus, qui sequitur mutationem consuetudium lectorum. Mirum est notare quam littera gothica, quam nunc putamus parum claram, anteposuerit litterarum formas humanitatis per seacula quarta decima et quinta decima.</p>
  <div class="heading-sample h1s">Heading 1</div>
  <div class="heading-sample h2s">Heading 2</div>
  <div class="heading-sample h3s">Heading 3</div>
  <div class="heading-sample h4s">Heading 4</div>
  <div class="heading-sample h5s">Heading 5</div>
  <div class="heading-sample h6s">Heading 6</div>

  <aside class="sidebar-box box-books">
    <h3>Libri</h3>
    <ul><li>Lorem ipsum dolor sit amet</li><li>Consectetuer adipiscing elit</li><li>Sed diam nonummy nibh</li></ul>
  </aside>
  <aside class="sidebar-box box-papers">
    <h3>Pubblicazioni scientifiche</h3>
    <ul><li>Lorem ipsum dolor sit amet</li><li>Consectetuer adipiscing elit</li><li>Sed diam nonummy nibh</li></ul>
  </aside>
  <aside class="sidebar-box box-talks">
    <h3>Conferenze</h3>
    <ul><li>Lorem ipsum dolor sit amet</li><li>Consectetuer adipiscing elit</li><li>Sed diam nonummy nibh</li></ul>
  </aside>
</main>

<footer>
  <p class="footer-note">© 2011 Prof. Benedetto L. Caramuzza. All rights reserved.</p>
  <div class="social-links">
    <a href="#"><i></i>Agora</a>
    <a href="#"><i></i>Pipit</a>
    <a href="#"><i></i>Nexo</a>
    <a href="#"><i></i>Vidra</a>
  </div>
</footer>
</body>
</html>
```